Web Design for Solar Energy Consultancy Company

~ May 3, 2017 Update ~
As our project is rapidly progressing towards its completion, we started building up the list of designs that attracted the most of the team's attention. Additional submittals are still most welcome. Before submitting your proposal, however, we can recommend to review the concepts that received 4 stars as these are the ones that, in our opinion, most closely match the brief's requirements. Thank you!!
~ April 30, 2017 Update ~
The project deadline has been extended to attract a broader design community and to better tailor the final design to the requirements of the project.
A "light", "clean" (minimalistic), professionally looking, unique design is expected. Please, try to avoid industry cliches. Also, please use green, which became another industry cliche, with great caution. The brief provides minimum details to foster creativity. With the same notion in mind, the page content information is not provided.
Thank you for your feedback and support of the project!!
~ April 22, 2017 Update ~
Additional comments after starting receiving more designs:
- your attention to the brief's requirements will be highly appreciated. It is expected that the design is unique - standard, commonly used, images, formats and approaches do not fall under this category. There is no need to "bombard" with slightly different variations of the same design. It is expected that a conceptual (preliminary) design is submitted first, and, after it is reviewed (each design will receive a star rating and, if the star rating is greater than 3, a detailed feedback), the requested changes are implemented. We believe this will allow to approach the design process more efficiently and safe additional time to both the Designers's Community and our company. Thank you for understanding.
Clarification, please submit two variations of a design:
1) 1 page "business card" design that the company will be able to use during its startup stage;
2) the fully functional design (as per the requirements outlined below) for the company to transition to after the start-up period is over. Same design principles as developed for option 1 should be used for this variation.
Additional clarification, please note that the news block will not require images (at least during the start-up stage). It is envisioned to be a news feeder.
~ April 21, 2017 Update ~
Preliminary comments after receiving first designs:
- please try to create a unique design, using common elements wisely. Though such solar energy "attributes" as a solar panel or a bulb are very well recognized and allow quickly identify the nature of the business, they also became so common that in many cases a design may seem very similar to the one of others (Oh!, I've already seen this... effect).
- please try to introduce the company's logo unobtrusively. The size and position of the logo should clearly identify the company, but the message should be subtle, the logo should not distract from the main design. Brevam's swoosh did not need to occupy have the screen.
- please use the green color with caution as it was with the company's logo. True, it is a green energy. But there is no need for the color to "scream" about it. Use the amount of green and its tone (avoid acid green) wisely.
--------------------------------------------------------------------------------
1. Main Goal
Develop a website that can represent the company to the industry stakeholders and become its "business card" during the start-up stage.
2. Secondary Goal
Develop a structure of a fully functional website that the "business card" design can eventually be transformed to staying consistent with the original design principles.
3. Key Audience
Varlo Corp. is providing consulting and technical services in the area of Solar Energy. The industry stakeholders include project developers, financial community, governmental bodies, OEMs, and competition.
4. Site Map
- HOME
• About
• Services
• Solar Energy
• News
• Contacts
• Social Media
- SERVICES*
- PROJECTS*
- FINANCE*
- TRAINING*
- SOLAR (ENERGY)*
* Maybe inactive / partially functional during the start-up stage.
5. Technical Specifications
Online brochure website during the start-up stage with a capability to be eventually transformed to a fully functional website while preserving the original design principles.
The design to be appealing, "light", professional, and with an intuitive and easy to navigate interface. Modern coding principles supporting efficiency and security to be utilized. Newest industry trends in website coding will be welcome.
The website to be designed so that it would fit well a computer, tablet, or mobile phone screen of any size. Cross-platform functionality to be taken into consideration to ensure that the website is fully functional on any platform.
Company's logo has already been designed and will be shared with the short-listed designers during the final design stage.
6. Interaction
The website will provide information about the company, our services, and projects. In addition, the industry insight, accumulated knowledge, and most recent trends are planned to be shared with stakeholders and attract and retain the audience.
Interaction with designers during the website development is envisioned to go through the following steps:
a) conceptual design - to be proposed by a designer originally. All conceptual designs will be reviewed and a feedback provided to pre-selected designers;
b) (preliminary and) final design - depending on the level of additional changes required can be broken into two steps. After discussing preliminary designs, company images will be provided to the selected finalists, who will compete with their final proposals.
7. Industry Stakeholders
- https://www.quelbrant.example/power/solar-power.- http://www.tavlorpeak.example/
- http://www.morvexaworks.example/about/company/
- https://www.pyxbel.example/energy/index.html
8. Budget
Defined by the project.
9. Timescale
Defined by the project.
12. Additional Info
- No copy-cats, standard graphics, or cliches please!
- Additional information / clarifications will be gladly provided upon request.
- This specification may be updated throughout the project to reflect discussions with / changes proposed by the Designers community.
Updates

```html
<!DOCTYPE html>
<html lang="en">
<head>
<meta charset="utf-8">
<title>Varlo Corp — Coming Soon</title>
<link href="https://fonts.googleapis.com/css2?family=Roboto:wght@400;500;700&family=Open+Sans:wght@400&display=swap" rel="stylesheet">
<style>
  :root {
    --white: #ffffff;
    --sky-grey: #7a7a7a;
    --haze: #5e5650;
    --dusk-brown: #3b2a20;
    --sun-amber: #b5651d;
    --deep-shadow: #1f1915;
    --accent-yellow: #ffb400;
    --logo-orange: #ffa800;
    --green-start: #079b47;
    --green-end: #8dc63f;
    --icon-dark: rgba(40, 32, 28, 0.75);
    --placeholder: #555555;
  }
  * { box-sizing: border-box; margin: 0; padding: 0; }
  html, body {
    width: 1200px;
    height: 772px;
    overflow: hidden;
  }
  body {
    position: relative;
    font-family: "Roboto", Arial, sans-serif;
    color: var(--white);
  }
  .hero-backdrop {
    position: absolute;
    inset: 0;
    background:
      radial-gradient(ellipse 260px 200px at 600px 360px, rgba(196, 112, 34, 0.55), transparent 70%),
      linear-gradient(180deg, var(--sky-grey) 0%, var(--haze) 38%, var(--dusk-brown) 62%, var(--deep-shadow) 100%);
  }
  .brand {
    position: absolute;
    left: 466px;
    top: 122px;
    display: flex;
    align-items: center;
    gap: 14px;
  }
  .brand-mark {
    width: 78px;
    height: 78px;
    border-radius: 50%;
    background: var(--logo-orange);
  }
  .brand-name {
    font-family: "Roboto", Arial, sans-serif;
    font-weight: 400;
    font-size: 40px;
    letter-spacing: 3px;
    line-height: 1;
    color: var(--white);
    padding-top: 30px;
  }
  .headline {
    position: absolute;
    left: 0;
    width: 100%;
    top: 318px;
    text-align: center;
    font-weight: 700;
    font-size: 74px;
    line-height: 1;
    letter-spacing: 0.5px;
  }
  .tagline {
    position: absolute;
    left: 0;
    width: 100%;
    top: 387px;
    text-align: center;
    font-size: 14.5px;
    font-weight: 400;
  }
  .subscribe-form {
    position: absolute;
    left: 336px;
    top: 436px;
    width: 530px;
    height: 49px;
    display: flex;
    background: var(--white);
    border-radius: 25px;
  }
  .subscribe-input {
    flex: 1;
    border: none;
    background: transparent;
    padding-left: 30px;
    font-family: "Open Sans", Arial, sans-serif;
    font-size: 13px;
    color: var(--placeholder);
    outline: none;
  }
  .subscribe-input::placeholder { color: var(--placeholder); }
  .subscribe-button {
    width: 150px;
    border: none;
    border-radius: 25px;
    background: linear-gradient(90deg, var(--green-start), var(--green-end));
    color: var(--white);
    font-family: "Roboto", Arial, sans-serif;
    font-weight: 500;
    font-size: 13.5px;
    text-transform: uppercase;
  }
  .social-links {
    position: absolute;
    left: 511px;
    top: 522px;
    display: flex;
    gap: 10px;
    list-style: none;
  }
  .social-link {
    width: 37px;
    height: 37px;
    border-radius: 50%;
    background: var(--icon-dark);
  }
  .social-link.is-active { background: var(--accent-yellow); }
  .copyright {
    position: absolute;
    left: 0;
    width: 100%;
    top: 712px;
    text-align: center;
    font-size: 13.5px;
  }
</style>
</head>
<body>
  <div class="hero-backdrop" role="img" aria-label="Photograph of a woman leaning on a wooden fence at sunset, dimmed with a dark overlay"></div>

  <header class="brand">
    <span class="brand-mark"></span>
    <span class="brand-name">VARLO CORP</span>
  </header>

  <main>
    <h1 class="headline">COMING SOON</h1>
    <p class="tagline">There has never been a better time to go solar.</p>

    <form class="subscribe-form">
      <input class="subscribe-input" type="email" placeholder="Enter Your Email Address">
      <button class="subscribe-button" type="button">Subscribe</button>
    </form>

    <ul class="social-links" aria-label="Social media">
      <li class="social-link"></li>
      <li class="social-link is-active"></li>
      <li class="social-link"></li>
      <li class="social-link"></li>
    </ul>
  </main>

  <footer class="copyright">Copyright 2017 Varlo Corp| All Right Reserved</footer>
</body>
</html>
```